Our branding needs something more.

We are a small all female law firm with an established brand and logo. We practice family, estate, and commercial law.
We're currently looking into a new website for our business but all the "standard" website templates are all the same and generally dull. We want to add some graphic elements to our branding that complement our identity and that will differentiate our website from all the others, - something that will make our website memorable.
We like our logo and don’t want to change it, but we want to add something extra to our branding to make it unique, reflect who we are, and stand-out. I’ve attached an image of our logo and a couple of designs we like. We’re thinking perhaps some doodles of images that are relevant to our legal work and that could tell a little story, either individually or in a sequence. Or maybe some random artistic splashes of colour?? All ideas are welcome, but they need to be appropriate for a legal business. We’re don’t want anything childishly cute or sweet colours.
Recapping, we’re an all female law firm looking for website branding that tells our story and differentiates us from every other boring website design. We may also use the new graphics on our stationary and Socials so flexibility to do this would be an advantage.
Please reach out if you have any questions.
Tess.

Target Market(s)

People (mainly women) looking for lawyers

Industry/Entity Type

Legal.

Requirements
Must have
• Outside the box.
Nice to have
• We’ll know it when we see it.
Should not have
• a cold corporate look.

```html
<!DOCTYPE html>
<html lang="en">
<head>
<meta charset="utf-8">
<title>Ashby Legal — Home</title>
<link href="https://fonts.googleapis.com/css2?family=Arimo:wght@400;700&display=swap" rel="stylesheet">
<style>
  :root {
    --ink: #403c3d;
    --brand-blue: #1c5cae;
    --nav-active: #1f5fd8;
    --hero-bg: #e2eefb;
    --art-tone: #cfdff1;
    --white: #ffffff;
  }
  * { box-sizing: border-box; margin: 0; padding: 0; }
  html, body { width: 1200px; height: 766px; overflow: hidden; }
  body {
    font-family: "Arimo", Arial, Helvetica, sans-serif;
    color: var(--ink);
    background: var(--hero-bg);
    position: relative;
  }
  .site-header {
    position: absolute; left: 0; top: 0;
    width: 1200px; height: 79px;
    background: var(--white);
  }
  .brand {
    position: absolute; left: 71px; top: 11px;
    display: flex; align-items: center; gap: 36px;
    text-decoration: none;
  }
  .brand-circle {
    width: 58px; height: 58px; border-radius: 50%;
    border: 3px solid var(--brand-blue);
  }
  .brand-name {
    font-size: 27px; font-weight: 400;
    color: var(--brand-blue);
    letter-spacing: 0.5px;
  }
  .main-nav {
    position: absolute; top: 0; left: 0; height: 79px; width: 1200px;
  }
  .main-nav a {
    position: absolute; top: 81px; top: 81px;
    font-size: 13px; color: var(--ink); text-decoration: none;
    top: 81px;
  }
  .main-nav a { top: 81px; }
  .main-nav a { top: auto; bottom: 27px; }
  .main-nav .is-active { color: var(--nav-active); }
  .nav-home { left: 641px; }
  .nav-about { left: 745px; }
  .nav-services { left: 850px; }
  .nav-blog { left: 970px; }
  .nav-contact { left: 1064px; }

  .hero-copy {
    position: absolute; left: 50px; top: 254px; width: 620px;
    text-align: center;
  }
  .hero-title {
    font-size: 35.5px; font-weight: 700; line-height: 35px;
    margin-bottom: 39px;
  }
  .hero-text {
    font-size: 20.5px; line-height: 24.8px; font-weight: 400;
    margin-bottom: 24px;
  }
  .learn-more {
    font-weight: 700; color: var(--ink); text-decoration: underline;
    text-underline-offset: 2px;
  }
  .contact-button {
    display: inline-block; margin-top: 0;
    width: 156px; height: 49px; line-height: 45px;
    border: 1.5px solid var(--ink);
    font-size: 22px; color: var(--ink); text-decoration: none;
  }
  .storefront-art {
    position: absolute; left: 680px; top: 148px;
    width: 460px; height: 510px;
    background: var(--art-tone);
    border-radius: 4px;
  }
</style>
</head>
<body>
  <header class="site-header">
    <a class="brand" href="#">
      <span class="brand-circle" aria-hidden="true"></span>
      <span class="brand-name">ASHBY LEGAL</span>
    </a>
    <nav class="main-nav">
      <a class="nav-home is-active" href="#">Home</a>
      <a class="nav-about" href="#">About</a>
      <a class="nav-services" href="#">Services</a>
      <a class="nav-blog" href="#">Blog</a>
      <a class="nav-contact" href="#">Contact</a>
    </nav>
  </header>

  <main>
    <section class="hero-copy">
      <h1 class="hero-title">Experience you can trust.<br>Results you can count on.</h1>
      <p class="hero-text">Ashby Legal, is a boutique law firm based in NSW, Australia specializing in all things associated with Estate Planning, Wills, Estate Administration, Estate Litigation and Family Provision Claim.</p>
      <p class="hero-text">We also provide services in property, such as conveyancing and family law matters. With over 20 years of experience we can provide effective legal representation. <a class="learn-more" href="#">LEARN MORE</a></p>
      <a class="contact-button" href="#">Contact</a>
    </section>

    <div class="storefront-art" role="img" aria-label="Line drawing of the firm's brick shopfront with its sign above the door, and a group of professional women standing and walking in front of it"></div>
  </main>
</body>
</html>
```